Lectres app for Android

We need design for Android application for selling audio lectures. The author of the lectures is a fairly well-known philologist and writer who has lectured on various topics (film, literature, etc.)

Design for the same iOS app has been succesfuly developed about nine month ago.

Design have to be developed for both tablet and phone in the "Matherial design" style and with colours as at existing app (see attachments).

There are 5 screens in this application.

1. Splash screen with application title "Vurda's library". This screen appears for 2-3 seconds at the app start.

2. Screen with a list of lectures. There must be the Author's photo (logo) and the app title in the screen as well as the list of lectures (starting from the last one) with pictures. The sketch in the attachment. Each lecture must have a category mark (movies, literature) as well as the title and a short description. In the list must be some difference between fully listened to lectures, thouse that haven't been listened to to the end. And thouse haven't been purchased yet. In the attached layout it is marked with the color of the ring next to each item. We need small palaying status at the bottom of the screen In the phone design (see attachment).
3. Player screen..It is desirable to see the progress of the lectures, title, lectures picture^ an opportunity to download it for listening offline, an icon to mark the lecture as the listened to, total duration and current position. .

4. Purchase screen

5. Info screen with some app settings (restore purchase, entering promo code and change a language).

The design should be in the "Material design" style and with colours as in the iOS app.

See existing iOS design in the files iOS4-iOS4.png

```html
<!DOCTYPE html>
<html lang="en">
<head>
<meta charset="utf-8">
<title>Vurda's library – Now Playing</title>
<link href="https://fonts.googleapis.com/css2?family=Roboto:wght@400;500&display=swap" rel="stylesheet">
<style>
  :root {
    --status-orange: #e9541f;
    --bar-orange: #ff5a24;
    --accent: #f4622a;
    --white: #ffffff;
    --ink: #333333;
    --muted: #555555;
    --track: #4a4a4a;
    --panel: rgba(88, 88, 88, 0.62);
    --photo-light: #c9c9c9;
    --photo-mid: #6e6e6e;
    --photo-dark: #141414;
  }
  * { box-sizing: border-box; margin: 0; padding: 0; }
  html, body { width: 675px; height: 1200px; overflow: hidden; background: var(--white); }
  body { font-family: 'Roboto', Arial, sans-serif; position: relative; }

  .status-bar {
    position: absolute; left: 0; top: 0; width: 675px; height: 45px;
    background: var(--status-orange);
  }
  .status-icons { position: absolute; right: 18px; top: 10px; display: flex; align-items: center; gap: 8px; }
  .status-time { color: var(--white); font-size: 24px; line-height: 26px; }

  .app-bar {
    position: absolute; left: 0; top: 45px; width: 675px; height: 103px;
    background: var(--bar-orange);
  }
  .menu-icon { position: absolute; left: 35px; top: 37px; }
  .app-title {
    position: absolute; left: 119px; top: 27px;
    color: var(--white); font-size: 36px; font-weight: 400; line-height: 44px;
  }
  .more-icon { position: absolute; left: 624px; top: 34px; }

  .lecture-stage { position: absolute; left: 0; top: 148px; width: 675px; height: 937px; }
  .lecture-photo {
    position: absolute; inset: 0;
    background: radial-gradient(ellipse at 48% 35%, #8a8a8a 0%, transparent 55%),
                linear-gradient(180deg, var(--photo-light) 0%, var(--photo-mid) 35%, #2a2a2a 62%, var(--photo-dark) 100%);
  }
  .transcript {
    position: absolute; left: 18px; top: 20px; width: 640px; height: 901px;
    background: var(--panel); border-radius: 3px;
    box-shadow: 0 2px 4px rgba(0,0,0,0.35);
    padding: 18px 0 0 17px;
  }
  .transcript p {
    color: var(--white); font-size: 20.6px; line-height: 23.9px; white-space: nowrap;
  }

  .player-bar {
    position: absolute; left: 0; top: 1085px; width: 675px; height: 115px;
    background: var(--white);
  }
  .pause-button { position: absolute; left: 22px; top: 37px; }
  .time-remaining { position: absolute; left: 79px; top: 50px; font-size: 14px; color: var(--ink); }
  .time-total { position: absolute; left: 545px; top: 50px; font-size: 15px; color: var(--accent); }
  .track-title {
    position: absolute; left: 0; width: 675px; top: 11px; text-align: center;
    font-size: 15px; color: var(--ink);
  }
  .track-author {
    position: absolute; left: 0; width: 675px; top: 33px; text-align: center;
    font-size: 11px; color: var(--accent);
  }
  .track-category {
    position: absolute; left: 0; width: 675px; top: 76px; text-align: center;
    font-size: 11px; color: var(--accent);
  }
  .progress { position: absolute; left: 141px; top: 51px; width: 383px; height: 15px; }
  .progress-played { position: absolute; left: 0; top: 0; width: 313px; height: 15px; background: var(--accent); border-radius: 3px 0 0 3px; }
  .progress-left { position: absolute; left: 321px; top: 0; width: 62px; height: 15px; background: var(--track); border-radius: 0 3px 3px 0; }
  .download-button { position: absolute; left: 614px; top: 40px; }
</style>
</head>
<body>
  <header class="status-bar">
    <div class="status-icons">
      <svg width="20" height="20" viewBox="0 0 20 20"><path d="M20 0 L20 20 L0 20 Z" fill="#ffffff" opacity="0.55"/><path d="M20 8 L20 20 L8 20 Z" fill="#ffffff"/></svg>
      <svg width="14" height="22" viewBox="0 0 14 22"><rect x="4" y="0" width="6" height="3" fill="#ffffff"/><rect x="0" y="3" width="14" height="19" rx="1.5" fill="#ffffff" opacity="0.55"/><rect x="0" y="9" width="14" height="13" rx="1.5" fill="#ffffff"/></svg>
      <span class="status-time">12:30</span>
    </div>
  </header>

  <nav class="app-bar">
    <svg class="menu-icon" width="34" height="24" viewBox="0 0 34 24"><rect y="0" width="34" height="3.5" fill="#ffffff"/><rect y="10" width="34" height="3.5" fill="#ffffff"/><rect y="20" width="34" height="3.5" fill="#ffffff"/></svg>
    <h1 class="app-title">Now Playing</h1>
    <svg class="more-icon" width="12" height="34" viewBox="0 0 12 34"><circle cx="6" cy="4" r="3.8" fill="#ffffff"/><circle cx="6" cy="17" r="3.8" fill="#ffffff"/><circle cx="6" cy="30" r="3.8" fill="#ffffff"/></svg>
  </nav>

  <main class="lecture-stage">
    <div class="lecture-photo" role="img" aria-label="Black and white portrait photograph of the lecture's subject"></div>
    <article class="transcript">
      <p>&nbsp;&nbsp;&nbsp;&nbsp;Lorem ipsum dolor sit amet, consectetuer adipiscing elit,<br>sed diam nonummy nibh euismod tincidunt ut laoreet<br>dolore magna aliquam erat volutpat. Ut wisi enim ad minim<br>veniam, quis nostrud exerci tation ullamcorper suscipit lob-<br>ortis nisl ut aliquip ex ea commodo consequat. Duis autem<br>vel eum iriure dolor in hendrerit in vulputate velit esse mo-<br>lestie consequat, vel illum dolore eu feugiat nulla facilisis at<br>vero eros et accumsan et iusto odio dignissim qui blandit<br>praesent luptatum zzril delenit augue duis dolore te feugait<br>nulla facilisi.</p>
      <p>&nbsp;&nbsp;&nbsp;&nbsp;Lorem ipsum dolor sit amet, consectetuer adipiscing elit,<br>sed diam nonummy nibh euismod tincidunt ut laoreet<br>dolore magna aliquam erat volutpat. Ut wisi enim ad minim<br>veniam, quis nostrud exerci tation ullamcorper suscipit lob-<br>ortis nisl ut aliquip ex ea commodo consequat. Duis autem<br>vel eum iriure dolor in hendrerit in vulputate velit esse mo-<br>lestie consequat, vel illum dolore eu feugiat nulla facilisis at<br>vero eros et accumsan et iusto odio dignissim qui blandit<br>praesent luptatum zzril delenit augue duis dolore te feugait<br>nulla facilisi.</p>
    </article>
  </main>

  <footer class="player-bar">
    <svg class="pause-button" width="35" height="43" viewBox="0 0 35 43"><rect x="0" y="0" width="11" height="43" rx="3" fill="#333333"/><rect x="24" y="0" width="11" height="43" rx="3" fill="#333333"/></svg>
    <span class="time-remaining">-59:58</span>
    <div class="track-title">Philosophy of Love in the Western World</div>
    <div class="track-author">by Mira Delacourt</div>
    <div class="progress">
      <div class="progress-played"></div>
      <div class="progress-left"></div>
    </div>
    <div class="track-category">Lectures | Philosophy</div>
    <span class="time-total">35:02</span>
    <svg class="download-button" width="40" height="38" viewBox="0 0 40 38"><path d="M14 0 H26 V14 H36 L20 30 L4 14 H14 Z" fill="#f4622a"/><rect x="1" y="33" width="38" height="5" fill="#f4622a"/></svg>
  </footer>
</body>
</html>
```